Sign for Pilates Studio

Cute and fun sandwich board sign ( 36" x 24" ) for outstanding Pilates studio in Santa Cruz. Sign should have logo, use the phrase "Pilates & Kinovane classes 7 Days a Week"
Updates

Dimensions are 36" x 24" and it should be clear and simple. The goal is to get people in the door. Try using the tree theme or the circle theme. Colors can be simple green, gold, burgundy....black lettering probably... Added Monday, January 12, 2015

Target Market(s)

Hip 30 year olds and everyone else too

Requirements
Must have
• It's a freestanding sign and should be simple to read
• Must say "Lark Hollow Pilates"
• "Pilates Classes 7 days A week"
Nice to have
• Logo, tree. green and gold colors
Should not have
• Not too busy. Easy to read while driving by

```html
<!DOCTYPE html>
<html lang="en">
<head>
<meta charset="utf-8">
<title>Lark Hollow Pilates – Sandwich Board Sign</title>
<link href="https://fonts.googleapis.com/css2?family=Anton&family=Archivo+Narrow:wght@700&family=Arimo:wght@400;700&display=swap" rel="stylesheet">
<style>
  :root {
    --page-bg: #e4e4e4;
    --poster-light: #e2ebc4;
    --poster-mid: #c9dba0;
    --leaf-green: #a9c98a;
    --leaf-soft: #bcd59a;
    --brand-green: #1e5b2b;
    --accent-green: #43a34f;
    --gold: #c9931f;
    --white: #ffffff;
  }
  html, body {
    margin: 0;
    width: 1200px;
    height: 1000px;
    overflow: hidden;
    background: var(--page-bg);
  }
  .sign {
    position: absolute;
    left: 300px;
    top: 50px;
    width: 600px;
    height: 900px;
    background: linear-gradient(180deg, var(--poster-light) 0%, var(--poster-mid) 100%);
    overflow: hidden;
    box-shadow: 0 6px 24px rgba(0,0,0,0.15);
  }
  .artwork {
    position: absolute;
    left: 150px;
    top: 170px;
    width: 450px;
    height: 560px;
    background: radial-gradient(ellipse at 60% 45%, var(--leaf-soft) 0%, var(--leaf-green) 45%, rgba(169,201,138,0) 75%);
  }
  .brand {
    position: absolute;
    left: 40px;
    top: 40px;
    right: 30px;
    height: 100px;
  }
  .brand-name {
    position: absolute;
    right: 0;
    top: 8px;
    margin: 0;
    font-family: "Arimo", Arial, sans-serif;
    font-weight: 700;
    font-size: 44px;
    line-height: 1.1;
    color: var(--brand-green);
    white-space: nowrap;
  }
  .brand-tagline {
    position: absolute;
    right: 0;
    top: 66px;
    margin: 0;
    padding: 3px 14px;
    background: var(--brand-green);
    color: var(--white);
    font-family: "Arimo", Arial, sans-serif;
    font-weight: 700;
    font-size: 15px;
    white-space: nowrap;
  }
  .schedule {
    position: absolute;
    left: 40px;
    top: 300px;
    height: 200px;
    font-family: "Archivo Narrow", "Arial Narrow", sans-serif;
    font-weight: 700;
  }
  .schedule-number {
    position: absolute;
    left: 0;
    top: -10px;
    font-size: 210px;
    line-height: 1;
    color: var(--gold);
  }
  .schedule-days {
    position: absolute;
    left: 90px;
    top: 0;
    font-size: 120px;
    line-height: 1;
    color: var(--accent-green);
  }
  .schedule-week {
    position: absolute;
    left: 90px;
    top: 118px;
    font-size: 64px;
    line-height: 1;
    color: var(--accent-green);
    white-space: nowrap;
  }
  .headline {
    position: absolute;
    left: 0;
    right: 0;
    top: 610px;
    text-align: center;
    margin: 0;
    font-family: "Anton", Impact, sans-serif;
    font-weight: 400;
    font-size: 175px;
    line-height: 1;
    letter-spacing: 0;
    color: var(--brand-green);
  }
  .subhead {
    position: absolute;
    left: 0;
    right: 0;
    top: 795px;
    text-align: center;
    margin: 0;
    font-family: "Arimo", Arial, sans-serif;
    font-weight: 400;
    font-size: 92px;
    line-height: 1;
    letter-spacing: 3px;
    color: var(--brand-green);
  }
</style>
</head>
<body>
  <main class="sign">
    <div class="artwork" role="img" aria-label="Faint leafy tree with a grey silhouette of a woman holding a Pilates bridge pose with one leg raised"></div>

    <header class="brand">
      <h1 class="brand-name">Lark Hollow Pilates</h1>
      <p class="brand-tagline">Pilates &amp; Kinovane Studio</p>
    </header>

    <div class="schedule">
      <span class="schedule-number">7</span>
      <span class="schedule-days">DAYS</span>
      <span class="schedule-week">A WEEK</span>
    </div>

    <h2 class="headline">PILATES</h2>
    <p class="subhead">CLASSES</p>
  </main>
</body>
</html>
```